【重要事項】
ワードプレスでのホームページ制作依頼、別途予定あり
デザインから制作まで一貫して行える方はご相談ください。
トップページデザインのみのご提案ももちろん大歓迎です。

【トップページデザインの要望】
・コンパクトでユーザーフレンドリー、お客様を意識したトップページ
サイトを訪れた人が求める情報にすぐアクセスできるデザインを希望します。詳細は添付ファイルをご覧ください。

【弊社ホームページ】
リニューアル対象のホームページURLのほか下記
http://rokugaen-shop.jp/
園芸のECサイトです。

【添付ファイル】
共有事項は添付ファイルにまとめています。お手数ですがご一読ください。
ロゴもございます。デザイン作成にお役立てください。
http://rokugaen.jp/
1ページ
緑系
• 高解像度JPG (.jpg)
• PNG形式 (.png)
8/31追記(質問への回答まとめ)

【納品形式の追加】
ai形式/PSD形式の納品可
※要望には個別でも柔軟に対応します。

【ロゴデータの追加】
pngデータ2つ、jpgデータ1つ
色のこだわりは強くありません。デザインに合わせてご活用ください。

【参考にしたいサイト】
https://q-m.co.jp/
最近できた会社様で、お客様目線に振り切ったデザインです。
ここまでポップにはできませんが、取り入れられる要素は取り入れたいと思っています。

https://www.nuvo-greno.com/
競合他社様ですが、多言語対応できるデザインレイアウトが印象的です。
弊社も英語対応のホームページ(弊社にて文言を翻訳)にする予定です。

みなさまのご応募お待ちしております。

当選者:桐山様
当選理由:社内会議による選考の末、多数決により決定しました。
色合いとデザインの段組が非常に優れておりました。
次点入選:blinker様、ree様
入選理由:blnker様は社内会議で最後まで当選作品と一、二を争う優秀作品でした。
特にイラストのテイストが社長の好みに合っており好印象でした。
ree様は写真の選定センス、全体のデザイン感が女性社員に受けました。

今回は担当が変わってから初めての提案でした。
不慣れなことが多い中、たくさんのご提案をいただき、様々な改善点や面白いデザイン、よりよいHPづくりのヒントをランサーのエキスパートの皆様よりいただきました。
誠にお礼申し上げます。

また、後半ご提出のご提案には、逐一ご挨拶ができず申し訳ございませんでした。
今回いただけた縁を活かして、よりよいHP制作につなげていきたいと考えております。

惜しくも当選、入選とならなかった皆様にも、心よりお礼を申し上げます。
またの機会がございましたら、よろしくお願いします。

```html
<!DOCTYPE html>
<html lang="ja">
<head>
<meta charset="utf-8">
<title>RokuGaen</title>
<link href="https://fonts.googleapis.com/css2?family=Lato:wght@400;700;900&family=Noto+Sans+JP:wght@300;400;500;700&display=swap" rel="stylesheet">
<style>
:root{
  --green:#5fd67a;
  --green-dark:#3fb85c;
  --ink:#222;
  --muted:#666;
  --line:#e3e3e3;
  --white:#fff;
  --dark:#555;
}
*{margin:0;padding:0;box-sizing:border-box}
html,body{width:1200px;height:5272px;overflow:hidden;background:var(--white)}
body{font-family:"Noto Sans JP",sans-serif;color:var(--ink);position:relative}
.abs{position:absolute}
.ph{position:absolute;display:block}

/* header */
.site-header{position:absolute;top:0;left:0;width:1200px;height:68px;display:flex;align-items:center;padding:0 36px;z-index:5;background:rgba(255,255,255,.94)}
.logo{font-family:"Lato",sans-serif;font-weight:900;font-size:28px;color:var(--ink);letter-spacing:.5px}
.nav{display:flex;gap:32px;margin-left:64px;font-family:"Lato",sans-serif;font-size:14px;font-weight:700}
.header-btns{margin-left:auto;display:flex;gap:12px}
.hbtn{height:40px;padding:0 18px;border-radius:6px;color:#fff;font-size:14px;display:flex;align-items:center;gap:8px;font-weight:500}
.hbtn.contact{background:var(--green)}
.hbtn.shop{background:var(--dark);font-family:"Lato",sans-serif;font-weight:700}

/* hero */
.hero{top:0;left:0;width:1200px;height:660px;
  background:
    radial-gradient(ellipse 140px 170px at 170px 400px,rgba(25,25,25,.75),rgba(25,25,25,0) 70%),
    radial-gradient(ellipse 120px 150px at 300px 420px,rgba(250,250,250,.8),rgba(250,250,250,0) 70%),
    radial-gradient(ellipse 150px 200px at 520px 380px,rgba(20,20,20,.8),rgba(20,20,20,0) 70%),
    radial-gradient(ellipse 120px 150px at 660px 360px,rgba(245,245,245,.75),rgba(245,245,245,0) 70%),
    radial-gradient(ellipse 170px 210px at 1000px 360px,rgba(25,25,25,.75),rgba(25,25,25,0) 70%),
    radial-gradient(ellipse 130px 160px at 1120px 420px,rgba(248,248,248,.8),rgba(248,248,248,0) 70%),
    radial-gradient(ellipse 420px 140px at 300px 120px,rgba(255,255,255,.85),rgba(255,255,255,0) 70%),
    radial-gradient(ellipse 380px 120px at 900px 150px,rgba(255,255,255,.8),rgba(255,255,255,0) 70%),
    linear-gradient(180deg,#6f9fd6 0%,#a9c8e8 30%,#d5e2ea 48%,#7d9a62 62%,#5b8d38 80%,#4a7a2c 100%)}
.hero-shade{top:0;left:0;width:1200px;height:660px;background:linear-gradient(180deg,rgba(0,0,0,0) 30%,rgba(0,0,0,.15) 50%,rgba(0,0,0,0) 70%)}
.hero-copy{position:absolute;top:284px;width:1200px;text-align:center;color:#fff;font-size:46px;font-weight:500;letter-spacing:3px;text-shadow:0 2px 10px rgba(0,0,0,.45)}
.side-tabs{position:absolute;left:0;top:168px;display:flex;flex-direction:column;gap:14px}
.side-tabs span{width:60px;height:200px;background:rgba(255,255,255,.9);border-radius:0 8px 8px 0;writing-mode:vertical-rl;display:flex;align-items:center;justify-content:center;font-size:14px;letter-spacing:2px}
.news{position:absolute;left:660px;top:512px;width:540px;background:rgba(255,255,255,.88);padding:12px 24px;font-size:13px}
.news li{list-style:none;display:flex;align-items:center;gap:14px;height:40px}
.news li+li{border-top:1px solid var(--line)}
.tag{background:var(--green);color:#fff;font-size:12px;padding:2px 12px;border-radius:3px;font-family:"Lato",sans-serif}

/* headings */
.sec-title{position:absolute;left:0;width:1200px;text-align:center}
.sec-title h2{font-family:"Lato",sans-serif;font-weight:400;font-size:44px;letter-spacing:2px;line-height:1.2}
.sec-title p{font-size:14px;margin-top:2px}

/* company */
.company-photo{top:768px;left:0;width:1200px;height:512px;
  background:
    radial-gradient(ellipse 60px 150px at 140px 990px,rgba(40,60,110,.9),rgba(40,60,110,0) 75%),
    radial-gradient(ellipse 50px 170px at 120px 200px,rgba(150,140,130,.9),rgba(150,140,130,0) 75%),
    radial-gradient(ellipse 40px 120px at 40px 220px,rgba(40,60,120,.85),rgba(40,60,120,0) 75%),
    radial-gradient(ellipse 60px 100px at 420px 200px,rgba(40,60,120,.8),rgba(40,60,120,0) 75%),
    radial-gradient(ellipse 380px 70px at 380px 260px,rgba(240,240,240,.95),rgba(240,240,240,0) 75%),
    radial-gradient(ellipse 300px 90px at 700px 110px,rgba(255,255,255,.6),rgba(255,255,255,0) 70%),
    linear-gradient(180deg,#3c66b4 0%,#7ea4d8 30%,#b9cee6 48%,#8da58a 56%,#6a9a3e 68%,#4d7f2b 100%)}
.company-card{position:absolute;left:704px;top:800px;width:448px;height:432px;background:rgba(255,255,255,.94);border-radius:20px;padding:76px 56px 0 88px;box-shadow:0 6px 20px rgba(0,0,0,.15)}
.company-card h3{font-family:"Lato",sans-serif;font-weight:400;font-size:48px;letter-spacing:2px;line-height:1.2}
.company-card .sub{font-size:14px;margin:0 0 22px}
.company-card .body{font-size:13px;line-height:1.7;color:var(--muted)}
.btn{display:flex;align-items:center;justify-content:center;background:var(--green);color:#fff;font-family:"Lato",sans-serif;font-weight:700;font-size:15px;border-radius:8px;letter-spacing:1px}
.company-card .btn{width:150px;height:38px;margin:40px 0 0 40px}

/* business */
.biz-card{position:absolute;top:1532px;width:488px;height:300px;border-radius:14px;overflow:hidden;box-shadow:0 4px 14px rgba(0,0,0,.15)}
.biz-card .label{position:absolute;bottom:0;left:0;right:0;height:52px;background:rgba(95,214,122,.95);color:#fff;font-size:20px;display:flex;align-items:center;justify-content:center;font-weight:500}
.label svg{position:absolute;right:18px;top:50%;transform:translateY(-50%)}
.biz-text{position:absolute;top:1864px;width:488px;font-size:14px;line-height:1.8;color:var(--muted)}

/* instagram */
.grass{position:absolute;background:linear-gradient(180deg,#a6e06c,#63b43f 60%,#4f9a34)}
.insta-grid{position:absolute;left:188px;top:2212px;width:812px;display:grid;grid-template-columns:repeat(4,195px);gap:10px}
.insta-grid i{display:block;height:195px;border-radius:4px}

/* blog */
.blog-card{position:absolute;top:2864px;width:304px;height:376px;background:#fff;box-shadow:0 4px 14px rgba(0,0,0,.15)}
.blog-card .thumb{height:180px}
.blog-card .in{padding:20px 22px}
.blog-card h4{font-size:16px;font-weight:500}
.blog-card .tag{display:inline-block;margin:12px 0}
.blog-card p{font-size:13px;color:var(--muted);line-height:1.6}

/* employee */
.emp-bg{top:3560px;left:0;width:1200px;height:330px;background:
  repeating-linear-gradient(90deg,rgba(0,0,0,0) 0 58px,rgba(180,180,180,.25) 58px 59px),
  linear-gradient(180deg,rgba(240,240,240,0),rgba(228,228,228,.7))}
.emp-card{position:absolute;top:3628px;width:312px;height:196px;border-radius:12px;overflow:hidden;box-shadow:0 4px 14px rgba(0,0,0,.15)}
.emp-card .label{position:absolute;bottom:0;left:0;right:0;height:40px;background:var(--green);color:#fff;font-size:15px;display:flex;align-items:center;justify-content:center}

/* recruit */
.recruit-photo{top:4020px;left:0;width:1200px;height:452px;
  background:
    radial-gradient(ellipse 150px 230px at 610px 320px,rgba(225,228,232,.95),rgba(225,228,232,0) 75%),
    radial-gradient(ellipse 70px 80px at 610px 110px,rgba(50,40,35,.7),rgba(50,40,35,0) 75%),
    radial-gradient(ellipse 150px 220px at 770px 380px,rgba(232,234,238,.95),rgba(232,234,238,0) 75%),
    radial-gradient(ellipse 70px 80px at 770px 200px,rgba(60,45,38,.65),rgba(60,45,38,0) 75%),
    radial-gradient(ellipse 180px 260px at 1000px 330px,rgba(236,238,242,.95),rgba(236,238,242,0) 75%),
    radial-gradient(ellipse 80px 90px at 1000px 90px,rgba(45,38,34,.7),rgba(45,38,34,0) 75%),
    linear-gradient(90deg,#efe9df 0%,#e2d8c9 45%,#cfc6b9 100%)}
.recruit-card{position:absolute;left:68px;top:4060px;width:444px;height:372px;background:rgba(255,255,255,.9);border-radius:18px;padding:52px 44px}
.recruit-card h3{font-family:"Lato",sans-serif;font-weight:400;font-size:48px;letter-spacing:2px;line-height:1.2}
.recruit-card .sub{font-size:14px;margin-bottom:20px}
.recruit-card .body{font-size:13px;line-height:1.7;color:var(--muted)}
.recruit-card .btn{width:190px;height:38px;margin:24px 0 0 40px}

/* access */
.access-btn{position:absolute;top:4760px;width:420px;height:84px;border-radius:8px;font-size:19px;display:flex;align-items:center;justify-content:center;gap:16px}
.access-btn.outline{border:2px solid var(--green);color:var(--green-dark);background:#fff}
.access-btn.fill{background:var(--green);color:#fff}

/* footer */
.site-footer{position:absolute;top:4948px;left:0;width:1200px;height:324px;border-top:1px solid var(--line)}
.site-footer .logo{position:absolute;left:54px;top:40px;font-size:26px}
.foot-offices{position:absolute;left:264px;top:40px;display:flex;gap:90px;font-size:13px;line-height:1.6}
.foot-offices b{font-weight:500}
.foot-offices span{color:var(--muted);font-size:12px}
.foot-nav{position:absolute;left:264px;top:150px;display:flex;gap:54px;font-size:13px;line-height:1.7}
.foot-nav div span{display:block;color:var(--muted);font-size:11px}
.copy{position:absolute;bottom:10px;width:100%;text-align:center;font-size:11px;color:#fff}
</style>
</head>
<body>

<section class="ph hero" role="img" aria-label="牧草地に並ぶ乳牛の写真"></section>
<div class="ph hero-shade"></div>
<header class="site-header">
  <div class="logo">RokuGaen</div>
  <nav class="nav"><span>COMPANY</span><span>BUSINESS</span><span>EMPLOYEE</span><span>RECRUIT</span><span>BLOG</span><span>ACCESS</span></nav>
  <div class="header-btns">
    <span class="hbtn contact"><svg width="16" height="12" viewBox="0 0 16 12"><rect x=".5" y=".5" width="15" height="11" rx="1" fill="none" stroke="#fff"/><path d="M1 1l7 6 7-6" fill="none" stroke="#fff"/></svg>お問い合わせ</span>
    <span class="hbtn shop">ONLINE SHOP</span>
  </div>
</header>
<div class="side-tabs"><span>農産物部門</span><span>畜産物部門</span></div>
<h1 class="hero-copy">動物や植物を通して豊かな生活を</h1>
<ul class="news">
  <li><span>2021.08.31</span><span class="tag">News</span><span>ホームページをリニューアルしました。</span></li>
  <li><span>2021.08.20</span><span class="tag">News</span><span>夏季休業のお知らせを掲載しました。</span></li>
</ul>

<section class="ph company-photo" role="img" aria-label="青空の下の牛舎とサイロの写真"></section>
<div class="company-card">
  <h3>COMPANY</h3>
  <p class="sub">会社について</p>
  <p class="body">テキストテキストテキストテキスト<br>テキストテキストテキストテキスト<br>テキストテキストテキストテキスト<br>テキストテキストテキストテキスト</p>
  <span class="btn">VIEW MORE</span>
</div>

<div class="sec-title" style="top:1392px"><h2>BUSINESS</h2><p>六雅園のおしごと</p></div>
<div class="biz-card" style="left:96px">
  <div class="ph" style="inset:0;background:
    radial-gradient(ellipse 160px 60px at 330px 190px,rgba(30,30,30,.7),rgba(30,30,30,0) 75%),
    radial-gradient(ellipse 120px 50px at 200px 200px,rgba(240,240,240,.7),rgba(240,240,240,0) 75%),
    radial-gradient(ellipse 120px 110px at 80px 110px,rgba(40,100,40,.85),rgba(40,100,40,0) 75%),
    linear-gradient(180deg,#5d95d8 0%,#a6c9ea 35%,#7eaa5a 60%,#4e8a32 100%)" role="img" aria-label="放牧された牛の写真"></div>
  <div class="label">畜産物部門・小動物部門<svg width="14" height="14" viewBox="0 0 14 14"><path d="M5 2l5 5-5 5" fill="none" stroke="#fff" stroke-width="2"/></svg></div>
</div>
<div class="biz-card" style="left:624px">
  <div class="ph" style="inset:0;background:
    radial-gradient(ellipse 80px 60px at 120px 130px,rgba(90,170,50,.9),rgba(90,170,50,0) 75%),
    radial-gradient(ellipse 90px 60px at 300px 120px,rgba(100,180,60,.9),rgba(100,180,60,0) 75%),
    radial-gradient(ellipse 70px 50px at 420px 140px,rgba(90,170,50,.85),rgba(90,170,50,0) 75%),
    linear-gradient(180deg,#d6e6c8 0%,#9dba7a 35%,#5e4a36 60%,#3e2c20 100%)" role="img" aria-label="畑に芽吹く苗の写真"></div>
  <div class="label">農産物部門・園芸部門<svg width="14" height="14" viewBox="0 0 14 14"><path d="M5 2l5 5-5 5" fill="none" stroke="#fff" stroke-width="2"/></svg></div>
</div>
<p class="biz-text" style="left:96px">テキストテキストテキストテキストテキストテキスト<br>テキストテキストテキストテキストテキストテキスト</p>
<p class="biz-text" style="left:624px">テキストテキストテキストテキストテキストテキスト<br>テキストテキストテキストテキストテキストテキスト</p>

<div class="sec-title" style="top:2028px"><h2>INSTAGRAM</h2></div>
<div class="grass" style="left:160px;top:2150px;width:880px;height:48px;border-radius:30px 30px 0 0" role="img" aria-label="草地と羊と豚のイラスト"></div>
<div class="insta-grid">
  <i role="img" aria-label="牛の写真" style="background:radial-gradient(ellipse at 40% 45%,#f2f2f2 0,#f2f2f2 18%,#2a2a2a 45%,#5a7a3a 100%)"></i>
  <i role="img" aria-label="牧草地の牛の写真" style="background:radial-gradient(ellipse 60px 40px at 50% 50%,#1f1f1f,rgba(31,31,31,0) 80%),linear-gradient(180deg,#a8c4d8 0%,#8cb860 35%,#5f9a3a 100%)"></i>
  <i role="img" aria-label="牛舎の写真" style="background:radial-gradient(ellipse 50px 30px at 50% 40%,#6a4a34,rgba(106,74,52,0) 80%),linear-gradient(180deg,#9fc88a,#3f7fb0 70%,#4f8ab8)"></i>
  <i role="img" aria-label="子牛の写真" style="background:radial-gradient(ellipse 70px 60px at 55% 50%,#8a5a3a,rgba(138,90,58,0) 80%),linear-gradient(180deg,#f0e8dc,#a8c0d8 60%,#8aa06a)"></i>
  <i role="img" aria-label="パンの写真" style="background:radial-gradient(circle at 30% 40%,#d49a5a,#a8682e 40%,#6a3e1e 100%)"></i>
  <i role="img" aria-label="牛の顔の写真" style="background:radial-gradient(ellipse at 55% 50%,#f5f5f5 0,#f5f5f5 20%,#262626 50%,#8aa6c8 100%)"></i>
  <i role="img" aria-label="作業の様子の写真" style="background:radial-gradient(ellipse 50px 60px at 60% 40%,#6a8ad8,rgba(106,138,216,0) 80%),linear-gradient(180deg,#e8e4e0,#b8b0a8 60%,#8a8078)"></i>
  <i role="img" aria-label="放牧の写真" style="background:radial-gradient(ellipse 90px 30px at 50% 60%,#222,rgba(34,34,34,0) 80%),linear-gradient(180deg,#b6d0e8,#dfe8ef 40%,#6c9e48 60%,#4d8030)"></i>
</div>

<div class="sec-title" style="top:2724px"><h2>BLOG</h2></div>
<article class="blog-card" style="left:96px"><div class="thumb" role="img" aria-label="鶏の写真" style="background:radial-gradient(ellipse 50px 70px at 25% 60%,#c88a4a,rgba(200,138,74,0) 80%),radial-gradient(ellipse 50px 70px at 60% 55%,#b8763c,rgba(184,118,60,0) 80%),linear-gradient(180deg,#e8e8e8,#8a5a34 60%,#5a3a20)"></div><div class="in"><h4>テキストテキストテキスト</h4><span class="tag">Blog</span><p>テキストテキストテキストテキスト<br>テキストテキストテキスト</p></div></article>
<article class="blog-card" style="left:444px"><div class="thumb" role="img" aria-label="土と苗の写真" style="background:radial-gradient(ellipse 70px 50px at 70% 40%,#7a9a4a,rgba(122,154,74,0) 80%),linear-gradient(160deg,#4a3c30,#2e241c 60%,#5a4634)"></div><div class="in"><h4>テキストテキストテキスト</h4><span class="tag">Blog</span><p>テキストテキストテキストテキスト<br>テキストテキストテキスト</p></div></article>
<article class="blog-card" style="left:800px"><div class="thumb" role="img" aria-label="牧場の牛の写真" style="background:radial-gradient(ellipse 120px 40px at 50% 62%,#2a2420,rgba(42,36,32,0) 80%),linear-gradient(180deg,#7fb0e0,#c8dcec 40%,#7aaa4a 60%,#5a8e32)"></div><div class="in"><h4>テキストテキストテキスト</h4><span class="tag">Blog</span><p>テキストテキストテキストテキスト<br>テキストテキストテキスト</p></div></article>
<span class="btn abs" style="left:504px;top:3292px;width:192px;height:40px">VIEW MORE</span>

<section class="ph emp-bg" role="img" aria-label="街並みの線画"></section>
<div class="sec-title" style="top:3484px"><h2>EMPLOYEE</h2><p>社員について</p></div>
<div class="emp-card" style="left:96px"><div class="ph" style="inset:0;background:radial-gradient(ellipse 40px 70px at 25% 70%,#3a9a68,rgba(58,154,104,0) 80%),radial-gradient(ellipse 40px 70px at 50% 70%,#3a9a68,rgba(58,154,104,0) 80%),radial-gradient(ellipse 40px 70px at 75% 70%,#3a9a68,rgba(58,154,104,0) 80%),linear-gradient(180deg,#e4efec,#c8dcd4)" role="img" aria-label="緑のエプロンの社員3名の写真"></div><div class="label">農産部社員</div></div>
<div class="emp-card" style="left:444px"><div class="ph" style="inset:0;background:radial-gradient(ellipse 50px 70px at 28% 70%,#eef0f2,rgba(238,240,242,0) 80%),radial-gradient(ellipse 50px 70px at 72% 70%,#eef0f2,rgba(238,240,242,0) 80%),linear-gradient(180deg,#dfe6ec,#a8b4be)" role="img" aria-label="作業着の社員3名の写真"></div><div class="label">企画部社員</div></div>
<div class="emp-card" style="left:792px"><div class="ph" style="inset:0;background:radial-gradient(ellipse 50px 70px at 30% 70%,#f4f6f8,rgba(244,246,248,0) 80%),radial-gradient(ellipse 50px 70px at 75% 70%,#f4f6f8,rgba(244,246,248,0) 80%),linear-gradient(180deg,#e8eef2,#b4c4cc)" role="img" aria-label="白衣の研究職社員の写真"></div><div class="label">開発部社員</div></div>

<section class="ph recruit-photo" role="img" aria-label="作業着の社員3名の写真"></section>
<div class="recruit-card">
  <h3>RECRUIT</h3>
  <p class="sub">採用について</p>
  <p class="body">テキストテキストテキストテキストテキスト<br>テキストテキストテキストテキストテキスト<br>テキストテキストテキストテキスト</p>
  <span class="btn">VIEW MORE</span>
</div>

<div class="sec-title" style="top:4592px"><h2>ACCESS</h2><p>拠点について</p></div>
<div class="ph" style="left:344px;top:4640px;width:90px;height:104px;background:radial-gradient(ellipse at 50% 40%,#f4f4f4 0,#cfcfcf 40%,#2e2e2e 75%,rgba(46,46,46,0) 76%)" role="img" aria-label="犬のイラスト"></div>
<div class="ph" style="left:740px;top:4640px;width:110px;height:104px;background:radial-gradient(ellipse at 50% 45%,#f6f0e6 0,#d9b27a 40%,#a9702e 72%,rgba(169,112,46,0) 74%)" role="img" aria-label="犬のイラスト"></div>
<span class="access-btn outline" style="left:132px">各営業所アクセス
  <svg width="24" height="24" viewBox="0 0 24 24"><circle cx="12" cy="16" r="5" fill="#3fb85c"/><circle cx="5" cy="9" r="2.5" fill="#3fb85c"/><circle cx="19" cy="9" r="2.5" fill="#3fb85c"/><circle cx="9" cy="4" r="2.5" fill="#3fb85c"/><circle cx="15" cy="4" r="2.5" fill="#3fb85c"/></svg></span>
<span class="access-btn fill" style="left:648px">各種お問い合わせ
  <svg width="24" height="24" viewBox="0 0 24 24"><circle cx="12" cy="16" r="5" fill="#fff"/><circle cx="5" cy="9" r="2.5" fill="#fff"/><circle cx="19" cy="9" r="2.5" fill="#fff"/><circle cx="9" cy="4" r="2.5" fill="#fff"/><circle cx="15" cy="4" r="2.5" fill="#fff"/></svg></span>

<footer class="site-footer">
  <div class="logo">RokuGaen</div>
  <div class="foot-offices">
    <div><b>本社事務所</b><br><span>〒000-0000<br>住所テキストテキスト</span></div>
    <div><b>北部事務所</b><br><span>〒000-0000<br>住所テキストテキスト</span></div>
    <div><b>南部事務所</b><br><span>〒000-0000<br>住所テキストテキスト</span></div>
  </div>
  <div class="foot-nav">
    <div>会社について<span>会社概要</span></div>
    <div>六雅園のおしごと<span>畜産物部門</span><span>農産物部門</span></div>
    <div>社員について<span>社員紹介</span></div>
    <div>採用について<span>募集要項</span></div>
    <div>ブログ</div>
    <div>拠点について<span>アクセス</span><span>お問い合わせ</span></div>
  </div>
  <div class="grass" style="left:0;bottom:0;width:1200px;height:48px" role="img" aria-label="草地と鶏のイラスト"></div>
  <p class="copy">© RokuGaen All Rights Reserved.</p>
</footer>

</body>
</html>
```